Professional Single Page Website Design for Vellowind Advisory

Vellowind Advisory is a new business consultancy specializing in providing expert services to small businesses, primarily in the brick-and-mortar retail and food service sectors. We offer a range of services including franchise development and launch, due diligence, and construction management.

Currently, we have a basic website set up at www.vellowindadvisory.example, but we need a professional touch to enhance its design and functionality.

Project Requirements:
- Single Page Design: For now, we need a single page design that effectively showcases who we are, our services, and contact information.
- Future Expansion: The design should be flexible and scalable for future expansion to include additional pages like specific service offerings, about us, and a dedicated contact page.
- Design Aesthetic: We are looking for a modern yet professional design that aligns with our brand identity.
- Logo: We have a logo that we like, which was also sourced from Pixel Forum. The logo files are attached to this project brief.

Key Sections to Include:
- Hero Section: An engaging introduction to Vellowind Advisory with a strong visual impact.
- About Us: A brief overview of who we are and our mission.
- Team: Section for the profiles of the two principals.
- Services: A clear and concise presentation of our services, including franchise development, due diligence, and construction management.
- Contact Information: Easy-to-find contact details, including a form for inquiries.
- Call to Action: Encouraging visitors to get in touch with us for consultations or further information.

Design Considerations:
- Ensure the design is responsive and mobile-friendly.
- Include high-quality images and icons that complement our services and industry.
- We do not need development services, this is only a design project.

```html
<!DOCTYPE html>
<html lang="en">
<head>
<meta charset="utf-8">
<title>Vellowind Advisory</title>
<link href="https://fonts.googleapis.com/css2?family=Poppins:ital,wght@0,300;0,400;0,500;0,600;0,700;1,400&display=swap" rel="stylesheet">
<style>
:root{
  --mint:#8fcaae;
  --mint-soft:#c9e6d8;
  --accent:#5fc08f;
  --navy:#1f2a36;
  --navy-deep:#18212b;
  --ink:#222;
  --body:#444;
  --grey-bg:#f4f4f4;
  --white:#fff;
}
*{margin:0;padding:0;box-sizing:border-box}
html,body{width:1200px;height:5038px;overflow:hidden}
body{font-family:'Poppins',sans-serif;color:var(--ink);background:var(--white);position:relative}
.abs{position:absolute}
/* header */
.site-header{position:absolute;left:0;top:0;width:1200px;height:118px;background:var(--white)}
.brand{position:absolute;left:78px;top:36px;display:flex;align-items:center;gap:14px}
.brand-dot{width:44px;height:44px;border-radius:50%;background:var(--mint)}
.brand-name{font-weight:600;font-size:24px;color:var(--navy)}
.main-nav{position:absolute;top:50px;left:612px;display:flex;gap:36px;font-size:14px;color:var(--navy)}
.main-nav .active{color:var(--mint);position:relative}
.main-nav .active::after{content:"";position:absolute;left:0;right:0;top:26px;height:2px;background:var(--mint)}
/* hero */
.hero{position:absolute;left:0;top:118px;width:1200px;height:727px;background:linear-gradient(180deg,#8fc9ad 0%,#a8d4bf 45%,#7fb79c 100%)}
.hero-photo{position:absolute;right:40px;top:120px;width:420px;height:480px;border-radius:40px;background:linear-gradient(135deg,#5f8c7a,#8dbfa7)}
.hero-panel{position:absolute;left:0;top:157px;width:610px;height:427px;background:rgba(200,232,216,.55);border-radius:0 24px 24px 0}
.hero h1{position:absolute;left:76px;top:200px;font-size:58px;font-weight:700;line-height:1;color:var(--navy)}
.hero .sub1{position:absolute;left:76px;top:268px;font-size:45px;font-weight:400;color:var(--navy)}
.hero .sub2{position:absolute;left:76px;top:350px;font-size:38px;line-height:46px;font-weight:400;color:var(--navy)}
.btn{display:inline-flex;align-items:center;justify-content:center;background:var(--navy);color:var(--white);border-radius:30px;font-weight:500;text-transform:uppercase}
.hero .btn{position:absolute;left:78px;top:476px;width:190px;height:58px;font-size:16px}
/* section heading */
.sec-head{position:absolute;display:flex;align-items:center;gap:18px}
.sec-head .mark{width:90px;height:90px;border-radius:50%;border:8px solid var(--mint)}
.sec-head h2{font-size:50px;font-weight:600;line-height:1;color:var(--navy)}
.sec-head p{font-size:32px;line-height:1;color:var(--mint);margin-top:2px}
/* about */
.about-photo{position:absolute;left:76px;top:980px;width:477px;height:452px;border-radius:28px;background:linear-gradient(160deg,#3b4654,#1f2833)}
.about-text{position:absolute;left:644px;top:1103px;width:424px;font-size:13px;line-height:27px;color:var(--body);text-align:justify}
.about-btn{position:absolute;left:645px;top:1380px;width:163px;height:50px;font-size:13px}
/* services */
.service{position:absolute;top:1755px;width:360px;text-align:center}
.diamond{width:250px;height:250px;margin:50px auto 0;transform:rotate(45deg);border-radius:60px;border:14px solid var(--mint-soft)}
.service h3{margin-top:72px;font-size:25px;font-weight:600;color:var(--navy)}
.service p{margin:8px auto 0;width:270px;font-size:13px;line-height:22px;color:var(--body)}
/* team */
.team-bg{position:absolute;left:0;top:2345px;width:1200px;height:937px;background:var(--grey-bg)}
.card{position:absolute;top:2620px;width:375px;height:510px;background:var(--white);box-shadow:0 2px 8px rgba(0,0,0,.08);text-align:center}
.card .portrait{width:178px;height:178px;margin:58px auto 0;transform:rotate(45deg);border-radius:50px}
.card h3{margin-top:54px;font-size:22px;font-weight:600;color:var(--navy)}
.card .role{font-size:18px;color:var(--accent)}
.card .bio{margin:12px auto 0;width:300px;font-size:13px;line-height:22px;color:var(--body)}
.card .more{font-size:12px;font-style:italic;color:var(--mint);text-decoration:underline}
.card .icons{display:flex;justify-content:center;gap:18px;margin-top:8px}
.round{width:46px;height:46px;border-radius:50%;background:var(--navy);display:flex;align-items:center;justify-content:center}
/* contact */
.contact-lead{position:absolute;left:0;top:3528px;width:1200px;text-align:center;font-size:22px;color:var(--ink)}
.contact-box{position:absolute;left:76px;top:3630px;width:1049px;height:790px;background:var(--grey-bg)}
.info{position:absolute;left:143px;display:flex;align-items:center;gap:20px}
.info .round{width:74px;height:74px}
.info h4{font-size:20px;font-weight:600;color:var(--navy)}
.info p{font-size:13px;color:var(--navy)}
.form{position:absolute;left:470px;top:3697px;width:610px;height:675px;background:var(--white)}
.form label{position:absolute;left:72px;font-size:13px;font-weight:500;color:var(--navy)}
.field{position:absolute;border:1px solid #e4e4e4;box-shadow:0 1px 4px rgba(0,0,0,.06);font-size:12px;color:#999;padding:0 20px;display:flex;align-items:center}
.form .btn{position:absolute;left:216px;top:565px;width:178px;height:54px;font-size:16px;text-transform:uppercase}
/* footer */
.footer{position:absolute;left:0;top:4550px;width:1200px;height:420px;background:var(--navy);color:var(--white)}
.footer h4{font-size:22px;font-weight:500}
.foot-line{height:2px;background:var(--mint);margin-top:6px}
.links{position:absolute;left:208px;top:150px;width:132px}
.links ul{list-style:none;margin-top:18px}
.links li{font-size:13px;line-height:26px;display:flex;align-items:center;gap:8px}
.tick{width:9px;height:9px;border:1.5px solid var(--mint);transform:rotate(45deg)}
.foot-brand{position:absolute;left:420px;top:70px;width:280px;text-align:center}
.foot-brand .dot{width:96px;height:96px;border-radius:50%;background:var(--mint);margin:0 auto 14px}
.foot-brand .name{font-size:21px;font-weight:500}
.socials{display:flex;justify-content:center;gap:16px;margin-top:20px}
.socials span{width:30px;height:30px;border:2px solid var(--white);transform:rotate(45deg);border-radius:5px}
.details{position:absolute;left:764px;top:150px;width:200px}
.detail{display:flex;gap:16px;align-items:center;margin-top:20px;font-size:13px;line-height:16px}
.detail .d{width:28px;height:28px;border:2px solid var(--white);transform:rotate(45deg);border-radius:4px;flex:none}
.copy{position:absolute;left:0;top:4970px;width:1200px;height:68px;background:var(--navy-deep);color:var(--white);font-size:12px;display:flex;align-items:center;justify-content:center}
</style>
</head>
<body>

<header class="site-header">
  <div class="brand"><span class="brand-dot"></span><span class="brand-name">Vellowind Advisory</span></div>
  <nav class="main-nav">
    <span class="active">HOME</span><span>WHO WE ARE</span><span>OUR SERVICES</span><span>TEAM</span><span>CONTACT US</span>
  </nav>
</header>

<section class="hero" role="img" aria-label="Modern apartment building with mint tint">
  <div class="hero-photo" role="img" aria-label="Close view of building balconies"></div>
  <div class="hero-panel"></div>
  <h1>Building Success</h1>
  <div class="sub1">in Southern California</div>
  <div class="sub2">Expertise at Every Step:<br>From Planning to Execution</div>
  <span class="btn">Learn More</span>
</section>

<div class="about-photo" role="img" aria-label="Dark-toned apartment building exterior"></div>
<div class="sec-head" style="left:636px;top:995px">
  <span class="mark" style="width:78px;height:78px"></span>
  <div><h2 style="font-size:42px">About Us</h2><p style="font-size:24px">Who We Are</p></div>
</div>
<p class="about-text">Welcome to Vellowind Advisory, your trusted partner in navigating the complexities of the real estate and small business markets. Founded by industry veterans Dorian Halvey and Theo Marrick, we specialize in providing comprehensive services tailored to the unique needs of our clients. Whether you're a franchisee, a new restaurant owner, or a commercial real estate investor, our expertise in due diligence, construction management, and investment property evaluation ensures you make informed, strategic decisions.</p>
<span class="btn about-btn">Read More</span>

<div class="sec-head" style="left:388px;top:1580px">
  <span class="mark"></span>
  <div><h2>Our Services</h2><p>What We Do</p></div>
</div>
<div class="service" style="left:50px">
  <div class="diamond" role="img" aria-label="Team joining hands in agreement" style="background:linear-gradient(135deg,#d9a9a0,#6f7a78)"></div>
  <h3>Franchise Development</h3>
  <p>Comprehensive franchise setup from evaluation to launch for scalable business growth.</p>
</div>
<div class="service" style="left:420px">
  <div class="diamond" role="img" aria-label="Business documents and charts on a desk" style="background:linear-gradient(135deg,#2c4e7c,#d8c9a8)"></div>
  <h3>Due Diligence</h3>
  <p>Comprehensive franchise setup from evaluation to launch for scalable business growth.</p>
</div>
<div class="service" style="left:789px">
  <div class="diamond" role="img" aria-label="Team reviewing construction plans at a table" style="background:linear-gradient(135deg,#9fb3c8,#4c6a8f)"></div>
  <h3>Construction Management</h3>
  <p>Comprehensive franchise setup from evaluation to launch for scalable business growth.</p>
</div>

<div class="team-bg"></div>
<div class="sec-head" style="left:420px;top:2458px">
  <span class="mark"></span>
  <div><h2>Our Team</h2><p>Vellowind</p></div>
</div>
<div class="card" style="left:200px">
  <div class="portrait" role="img" aria-label="Portrait of principal Dorian Halvey" style="background:linear-gradient(135deg,#cfe3f2,#b7a9c9)"></div>
  <h3>Dorian Halvey</h3><div class="role">Principal</div>
  <p class="bio">Dorian Halvey brings almost 20 years of rich experience as a real estate investor</p>
  <div class="more">Read More</div>
  <div class="icons">
    <span class="round"><svg width="20" height="20" viewBox="0 0 24 24"><path d="M6.6 10.8a15 15 0 0 0 6.6 6.6l2.2-2.2c.3-.3.7-.4 1-.2 1.1.4 2.3.6 3.6.6.6 0 1 .4 1 1V20c0 .6-.4 1-1 1A17 17 0 0 1 3 4c0-.6.4-1 1-1h3.5c.6 0 1 .4 1 1 0 1.3.2 2.5.6 3.6.1.3 0 .7-.2 1z" fill="#fff"/></svg></span>
    <span class="round"><svg width="20" height="16" viewBox="0 0 20 16"><rect x="1" y="1" width="18" height="14" rx="1" fill="#fff"/><path d="M1 2l9 7 9-7" stroke="#1f2a36" stroke-width="1.5" fill="none"/></svg></span>
  </div>
</div>
<div class="card" style="left:625px">
  <div class="portrait" role="img" aria-label="Portrait of principal Theo Marrick" style="background:linear-gradient(135deg,#a9a295,#4d4a46)"></div>
  <h3>Theo Marrick</h3><div class="role">Principal</div>
  <p class="bio">Theo Marrick is a seasoned real estate expert with extensive experience in project</p>
  <div class="more">Read More</div>
  <div class="icons">
    <span class="round"><svg width="20" height="20" viewBox="0 0 24 24"><path d="M6.6 10.8a15 15 0 0 0 6.6 6.6l2.2-2.2c.3-.3.7-.4 1-.2 1.1.4 2.3.6 3.6.6.6 0 1 .4 1 1V20c0 .6-.4 1-1 1A17 17 0 0 1 3 4c0-.6.4-1 1-1h3.5c.6 0 1 .4 1 1 0 1.3.2 2.5.6 3.6.1.3 0 .7-.2 1z" fill="#fff"/></svg></span>
    <span class="round"><svg width="20" height="16" viewBox="0 0 20 16"><rect x="1" y="1" width="18" height="14" rx="1" fill="#fff"/><path d="M1 2l9 7 9-7" stroke="#1f2a36" stroke-width="1.5" fill="none"/></svg></span>
  </div>
</div>

<div class="sec-head" style="left:392px;top:3400px">
  <span class="mark"></span>
  <div><h2>Contact Us</h2><p>Get In Touch</p></div>
</div>
<p class="contact-lead">Encouraging visitors to get in touch with us for consultations or further information.</p>
<div class="contact-box"></div>
<div class="info" style="top:3828px">
  <span class="round"><svg width="26" height="34" viewBox="0 0 24 32"><path d="M12 0a12 12 0 0 0-12 12c0 9 12 20 12 20s12-11 12-20A12 12 0 0 0 12 0z" fill="#fff"/><circle cx="12" cy="12" r="4.5" fill="#1f2a36"/></svg></span>
  <div><h4>LOCATION</h4><p>Address line dummy Here</p></div>
</div>
<div class="info" style="top:4013px">
  <span class="round" style="background:var(--mint)"><svg width="30" height="30" viewBox="0 0 24 24"><path d="M6.6 10.8a15 15 0 0 0 6.6 6.6l2.2-2.2c.3-.3.7-.4 1-.2 1.1.4 2.3.6 3.6.6.6 0 1 .4 1 1V20c0 .6-.4 1-1 1A17 17 0 0 1 3 4c0-.6.4-1 1-1h3.5c.6 0 1 .4 1 1 0 1.3.2 2.5.6 3.6.1.3 0 .7-.2 1z" fill="#fff"/></svg></span>
  <div><h4>CALL US</h4><p>555 014 2290</p></div>
</div>
<div class="info" style="top:4203px">
  <span class="round"><svg width="34" height="26" viewBox="0 0 20 16"><rect x="1" y="1" width="18" height="14" rx="1" fill="#fff"/><path d="M1 2l9 7 9-7" stroke="#1f2a36" stroke-width="1.5" fill="none"/></svg></span>
  <div><h4>EMAIL US</h4><p>info@vellowindadvisory.example</p></div>
</div>

<form class="form">
  <label style="top:50px">TELL US YOUR NAME *</label>
  <div class="field" style="left:72px;top:70px;width:222px;height:44px">First Name:</div>
  <div class="field" style="left:312px;top:70px;width:228px;height:44px">Last Name:</div>
  <label style="top:153px">ENTER YOUR EMAIL *</label>
  <div class="field" style="left:72px;top:173px;width:468px;height:44px">Email:</div>
  <label style="top:256px">ENTER PHONE NUMBER</label>
  <div class="field" style="left:72px;top:276px;width:468px;height:44px">Phone:</div>
  <label style="top:360px">MESSAGE *</label>
  <div class="field" style="left:72px;top:380px;width:468px;height:152px;align-items:flex-start;padding-top:14px">Write us a message</div>
  <span class="btn">Submit Now</span>
</form>

<footer class="footer">
  <div class="links">
    <h4>Quik Links</h4><div class="foot-line"></div>
    <ul><li><span class="tick"></span>Home</li><li><span class="tick"></span>Who We Are</li><li><span class="tick"></span>Our Services</li><li><span class="tick"></span>Team</li><li><span class="tick"></span>Contact Us</li></ul>
  </div>
  <div class="foot-brand">
    <div class="dot"></div>
    <div class="name">Vellowind Advisory</div>
    <div class="socials"><span></span><span></span><span></span><span></span></div>
  </div>
  <div class="details">
    <h4>Contact Details</h4><div class="foot-line"></div>
    <div class="detail"><span class="d"></span><div>CALL US<br>555 014 2290</div></div>
    <div class="detail"><span class="d"></span><div>EMAIL US<br>info@vellowindadvisory.example</div></div>
    <div class="detail"><span class="d"></span><div>Address line here dummy<br>Address line here</div></div>
  </div>
</footer>
<div class="copy">Copyright © 2024 All Rights Reserved By Company name</div>

</body>
</html>
```